Product Description page for Hullwrap.com, References here just need a clean up redesign

Hi, were working on updating the product description page of our site hullwrap.com

Attached is a reference of what we drew on paint. We want to keep it pretty much the same as far as whats on there, the components with a few small adjustments and a clean actually designed look.

1. We want to remove the tabs (product description, warranty, reviews) and put it all in that main content area stretching down into sections. IE: Product Description section, followed by reviews, followed by warranty, below each other.
2. The side bar needs to be redesigned as far as the look and feel but the content and whats in there should stay the same.
3. The main banner area will be replaced shortly you do not have to worry about that.
4. Include a section or box for people to put in their email for a free Ebook.

Target Market(s)

people looking to easily view our boat cover products and buy without having to click too often or leave the page.

Industry/Entity Type

Online Shopping

Number of Pages Required

1 page

Requirements
Must have
• - Must update the sidebar
• - Must update the content area to remove the tabs and put the content from each tab sectioned off below each other (dummy text is fine for now for the tabs you cant view)
Nice to have
• - Cool place thats clean and functional to insert a section for people to put in their email to receive a free ebook
Should not have
• - too much change, we already know what we want and have a solid reference to work from.

```html
<!DOCTYPE html>
<html lang="en">
<head>
<meta charset="utf-8">
<title>Hullwrap.com – Boat Cover up to 16'8" Long and 90" Wide</title>
<link href="https://fonts.googleapis.com/css2?family=Arimo:wght@400;700&display=swap" rel="stylesheet">
<style>
:root{
  --navy:#0a2f7f;
  --navy-deep:#05215e;
  --navy-light:#1a4fb0;
  --ink:#333;
  --muted:#666;
  --soft:#888;
  --line:#c9c9c9;
  --tint:#f1fbfd;
  --tint-line:#9ccfd8;
  --stripe:#f5f5f5;
  --gold:#e5b21a;
  --white:#fff;
}
*{box-sizing:border-box;margin:0;padding:0}
html,body{width:1200px;height:2416px;overflow:hidden;background:var(--white);font-family:"Arimo",Arial,sans-serif;color:var(--ink)}
.page{position:relative;width:1200px;height:2416px}
.top-band{position:absolute;left:0;top:0;width:1200px;height:68px;background:linear-gradient(180deg,var(--navy-light),var(--navy-deep));}
.top-band h1{position:absolute;left:84px;top:21px;color:var(--white);font-size:22px;font-weight:700}
.crumbs{position:absolute;left:68px;top:103px;font-size:12px;color:#222}
.crumbs .current{color:#1d4fb8}
.card{position:absolute;left:68px;top:150px;width:1066px;height:2194px;border:1px solid var(--line);border-radius:14px;background:var(--white)}
.fits{position:absolute;left:100px;top:184px;width:1000px;height:50px;background:var(--tint);border:1px solid var(--tint-line);font-size:17px;color:#555;padding:15px 0 0 40px}
.hero{position:absolute;left:274px;top:282px;width:733px;height:290px;border-radius:40px 80px 20px 20px;background:radial-gradient(ellipse at 50% 40%,#d7d9dc,#b4b7bb 55%,#eef0f1 80%)}
.thumbs{position:absolute;left:228px;top:567px;display:flex;gap:8px}
.thumbs span{width:62px;height:62px;border:1px solid #ddd;background:linear-gradient(135deg,#7b8595,#3b4658)}
.thumbs span:nth-child(2){background:linear-gradient(135deg,#3d7fc6,#1b3f7a)}
.main{position:absolute;left:100px;width:685px}
.sec-head{height:32px;border:1px solid var(--tint-line);background:var(--tint);font-size:17px;color:#4a5b66;padding:7px 0 0 16px}
.sub{font-size:12px;color:#555;margin:0 0 6px 32px}
.body{font-size:11px;line-height:17px;color:var(--muted);margin:0 0 12px 32px;padding-right:10px}
.feat{display:grid;grid-template-columns:375px 270px;margin-left:32px;font-size:11px;line-height:21px;color:var(--muted)}
.review{padding:10px 16px 12px 16px}
.review.alt{background:var(--stripe)}
.review .who{display:flex;align-items:center;gap:14px;font-size:12px;color:#444;margin-bottom:8px}
.review p{font-size:12px;line-height:20px;color:#555}
.stars{display:flex;gap:2px}
.side{position:absolute;left:817px;width:290px;border:1px solid #999;border-radius:6px;overflow:hidden;background:var(--white)}
.side-head{background:linear-gradient(180deg,var(--navy-light),var(--navy-deep));color:var(--white);font-weight:700;font-size:16px;text-align:center;height:48px;padding-top:16px}
.price-head{font-size:26px;text-align:left;padding:11px 0 0 20px;height:52px}
.price-rows{padding:12px 24px 0 24px;font-size:14px}
.price-rows div{display:flex;justify-content:space-between;height:35.5px}
.price-rows s{color:#222}
.swatches{display:flex;gap:1px;margin-top:3px}
.swatches i{width:8px;height:8px;display:block}
.qty{width:80px;height:14px;border:1px solid #ccc;border-radius:2px;font-size:8px;text-align:right;padding-right:6px}
.actions{display:flex;justify-content:space-between;padding:10px 15px 0 15px}
.btn-cart{width:118px;height:32px;background:var(--navy);border-radius:4px;color:var(--white);font-size:12px;display:flex;align-items:center;gap:10px;padding-left:10px}
.badge-ship{width:120px;height:24px;margin-top:4px;background:var(--navy-light);color:var(--white);font-size:10px;font-weight:700;border-radius:3px;display:flex;align-items:center;gap:6px;padding-left:4px}
.badge-ship b{width:22px;height:22px;border-radius:50%;background:var(--gold)}
.fpt{display:flex;align-items:flex-start;padding:0 12px;height:108px}
.fpt:first-of-type{margin-top:28px}
.box{width:18px;height:18px;border:1px solid #777;margin-top:16px;flex:none}
.fpt-img{width:62px;height:64px;margin:0 10px 0 18px;flex:none;border-radius:4px;background:linear-gradient(135deg,#c8ccd2,#6c7480)}
.fpt h4{font-size:14px;font-weight:400;color:#222;margin-bottom:4px}
.fpt small{display:block;font-size:12px;color:var(--soft);line-height:15px}
.fpt strong{display:block;font-size:16px;color:var(--navy);margin-top:5px}
.indoor-img{width:170px;height:100px;margin:36px auto 30px;border-radius:40px 60px 10px 10px;background:linear-gradient(180deg,#2d7ad4,#1b4f95 60%,#c7c9cc)}
.center{text-align:center}
.indoor h4{font-size:16px;font-weight:400;line-height:21px;color:#222}
.indoor .reg{font-size:15px;margin-top:12px}
.indoor .deal{font-size:24px;font-weight:700;color:var(--navy);margin-top:8px}
.ebook{padding:44px 0 0 0}
.ebook-top{display:flex;gap:14px;padding-left:28px}
.ebook h4{font-size:18px;font-weight:400;color:#222;margin-top:6px}
.ebook small{font-size:12px;color:var(--soft)}
.ebook .field{margin:24px 0 0 22px;width:250px;height:28px;border:1px solid #ccc;border-radius:3px}
.ebook .submit{margin:18px auto 0;width:86px;height:26px;background:var(--navy);color:var(--white);font-size:12px;font-weight:700;text-align:center;padding-top:6px;border-radius:2px}
.hills{position:absolute;left:0;top:2344px;width:1200px;height:72px;background:linear-gradient(180deg,#fff 0%,#c9d8ea 45%,#6f8fba 100%)}
</style>
</head>
<body>
<div class="page">
  <header class="top-band"><h1>up to 16’8” Long and 90” Wide</h1></header>
  <nav class="crumbs">Home &gt; Boat Covers &gt; Center Console with Bow Rails &gt; <span class="current">up to 16'8" Long and 90" Wide</span></nav>

  <div class="card"></div>
  <div class="fits">Fits: Center Console with Bow Rails up to 16'8" Long and 90" Wide</div>
  <div class="hero" role="img" aria-label="Grey boat cover strapped over a center console boat on a trailer"></div>
  <div class="thumbs" role="img" aria-label="Product thumbnail gallery"><span></span><span></span><span></span><span></span><span></span><span></span></div>

  <section class="main" style="top:665px">
    <div class="sec-head">Product Information</div>
    <p class="sub" style="margin-top:20px">Description</p>
    <p class="body">When a boat is stored outside it is exposed to harmful elements such as wind, dirt, rain, and UV. The Keelguard Supreme is the most powerful cover available providing 10x more strength and protection compared to the competition. The 1200 denier fabric is 100% waterproof and provides excellent protection against sun, rain, wind and snow.</p>
    <p class="sub">Features</p>
    <div class="feat">
      <div>• 5 Star Fit. Fit guaranteed or your money back<br>• 10 Year Warranty. Full warranty covering rips and tears<br>• The covers comes in Grey, Blue and Maroon<br>• The fabric is pure 100% Marine Polyester (no cotton mix)<br>• No worries, the cover won't stretch or shrink<br>• The cover also comes with an integrated hem cord to be used when<br>&nbsp;&nbsp;mooring or on boat lifts</div>
      <div>• Rain or sleet the is 100% waterproof<br>• Fully Breathable, you'll never see mold or mildew<br>• UV resistant and also prevents heat buildup<br>• Fully Trailerable (straps included)<br>• Tough - Strong - Durable</div>
    </div>
  </section>

  <section class="main" style="top:1013px">
    <div class="sec-head">Reviews</div>
    <div style="height:8px"></div>
    <div class="review"><div class="who">Brandon J. <span class="stars"><svg width="86" height="16" viewBox="0 0 86 16"><defs><polygon id="st" points="8,0 10,5.5 16,5.8 11.3,9.6 13,15.5 8,12 3,15.5 4.7,9.6 0,5.8 6,5.5" fill="#e5b21a" stroke="#a87a08" stroke-width=".6"/></defs><use href="#st"/><use href="#st" x="17.5"/><use href="#st" x="35"/><use href="#st" x="52.5"/><use href="#st" x="70"/></svg></span></div><p>"This item is quite heavy duty and rides well. It is also great quality. We are pleased with the cover and I would recommend it to anyone who wants a great fit and strong cover."</p></div>
    <div class="review alt"><div class="who">Peter <span class="stars" style="margin-left:22px"><svg width="86" height="16" viewBox="0 0 86 16"><use href="#st"/><use href="#st" x="17.5"/><use href="#st" x="35"/><use href="#st" x="52.5"/><use href="#st" x="70"/></svg></span></div><p>"Great cover and very nice fit. Would buy again if needed. Highly recommend this cover. Ties down tight and snug.<br>Very high quality cover!"</p></div>
    <div class="review"><div class="who">Leroy <span class="stars" style="margin-left:22px"><svg width="86" height="16" viewBox="0 0 86 16"><use href="#st"/><use href="#st" x="17.5"/><use href="#st" x="35"/><use href="#st" x="52.5"/><use href="#st" x="70"/></svg></span></div><p>"This is a must have for your boat, cover does exactly what it supposed to do, fits well and seems to be made of really strong material so it should last a while."</p></div>
    <div class="review alt"><div class="who">Carlos <span class="stars" style="margin-left:18px"><svg width="86" height="16" viewBox="0 0 86 16"><use href="#st"/><use href="#st" x="17.5"/><use href="#st" x="35"/><use href="#st" x="52.5"/><use href="#st" x="70"/></svg></span></div><p>"I have this on my cruiser and it fits great. I feel better with my boat covered and this is a very nice cover. The price was nice especially if you have seen the price on factory covers. I would definitely buy this again and recommend to anyone with boat."</p></div>
  </section>

  <section class="main" style="top:1490px">
    <div class="sec-head">Warranty</div>
    <p class="sub" style="margin-top:18px">Returns &amp; Refunds</p>
    <p class="body">If you are not 100% satisfied with your purchase, you can return or exchange your order. (Returns must be unworn, in the state you received them, and in the original packaging).</p>
    <p class="body">Harbor Shield Covers will process all returns and refunds within 30 days of original order date. After 30 days all orders are final. For the full details on our returns or exchange policy please read below.</p>
    <p class="body">Harbor Shield Covers guarantees the covers you purchase will arrive in new condition, be free of defects and will properly fit the vehicle for which you ordered. If your item fails to meet the criteria above Harbor Shield Covers will exchange or return the item.</p>
    <p class="sub">Returning Keelguard Supreme Covers</p>
    <p class="body">Keelguard Supreme covers are 5 Star Fit Covers. The fit and quality are 100% guaranteed or your money back. You have 30 days to try the cover. If you are not 100% satisfied feel free to return or exchange it hassle free. No restocking fee's, we even pay for the shipping.</p>
    <p class="sub">Returning TideLine Covers</p>
    <p class="body">TideLine covers are 4 Star Fit Covers. TideLine covers are semi custom covers based on boat style, length and width. The cover is fully exchangeable.. A small 15% restocking fee is applied when returning or exchanging this cover. You have 30 days to return or exchange the cover. If you are not 100% satisfied, give us a call and will help return or exchange it. We even pay for the shipping.</p>
    <p class="sub">Returning SolarMarine Covers</p>
    <p class="body">SolarMarine covers are 3 Star Fit Covers. SolarMarine covers are universal covers based on length and width. A small 15% restocking fee is applied when returning or exchanging this cover. You have 30 days to return or exchange this cover. If you are not 100% satisfied, give us a call and will help return or exchange it. We even pay for the shipping.</p>
  </section>

  <section class="main" style="top:2003px">
    <div class="sec-head">Shipping</div>
    <p class="sub" style="margin-top:18px">Shipping</p>
    <p class="body">Unlike many other web sites that have special rules and lots of fine print, Harbor Shield Covers offers free shipping on all domestic orders placed on our website.</p>
    <p class="body">Just because shipping is free doesn't mean it should take a long time. We understand that getting your items quickly is important to you, so we make every effort to process your order quickly. When you order from our website, you can expect to receive your order within 4-5 business days.</p>
    <p class="body">If an error is found in the shipping address, please contact us at 1-800-555-0142 as soon as possible and our Support Staff will do their best.</p>
    <p class="sub">Shipping Internationally</p>
    <p class="body">We will gladly ship your product to Canada; however, these orders are not eligible for free shipping and may be subject to customs fees, taxes, or duties. These fees are not determined until the product crosses the border; therefore, these costs are the responsibility of the customer. Our shipping and handling cost does not include any of these fees.</p>
  </section>

  <aside class="side" style="top:585px;height:354px">
    <div class="side-head price-head">$ 331.50</div>
    <div class="price-rows">
      <div><span>Regular Price</span><s>$ 442.00</s></div>
      <div><span>You Save</span><span>$ 110.50</span></div>
      <div><span>Availability</span><span>Ready to ship</span></div>
      <div><span>Ships</span><span>1 Business Day</span></div>
      <div><span>Select Color <b style="color:#c00">*</b></span><span class="swatches"><i style="background:#d22"></i><i style="background:#e9c21b"></i><i style="background:#2a9a3a"></i><i style="background:#1aa5c9"></i><i style="background:#22409a"></i><i style="background:#888"></i><i style="background:#5b3a1c"></i><i style="background:#111"></i></span></div>
      <div><span>Quantity <b style="color:#c00">*</b></span><span class="qty">▾</span></div>
    </div>
    <div class="actions">
      <div class="btn-cart"><svg width="22" height="18" viewBox="0 0 22 18"><path d="M1 2h4l3 10h10l3-7H7" fill="none" stroke="#fff" stroke-width="1.6"/><circle cx="9" cy="15.5" r="1.6" fill="#fff"/><circle cx="17" cy="15.5" r="1.6" fill="#fff"/></svg>Add to Cart</div>
      <div class="badge-ship"><b></b>Free Shipping*</div>
    </div>
  </aside>

  <aside class="side" style="top:968px;height:398px">
    <div class="side-head">Frequently Purchased Together</div>
    <div class="fpt"><svg class="box" viewBox="0 0 18 18"><path d="M3 9l4 5 9-13" fill="none" stroke="#0a2f7f" stroke-width="3"/></svg><div class="fpt-img" role="img" aria-label="Support pole"></div><div><h4>Support Pole</h4><small>Works for boat and trucks!</small><strong>$ 30.75</strong></div></div>
    <div class="fpt"><svg class="box" viewBox="0 0 18 18"><path d="M3 9l4 5 9-13" fill="none" stroke="#0a2f7f" stroke-width="3"/></svg><div class="fpt-img" style="background:linear-gradient(135deg,#3d63b8,#13275e)" role="img" aria-label="Navy boat motor cover"></div><div><h4>Boat Motor Cover</h4><small>Heavy duty waterproof material</small><strong>$ 43.06</strong></div></div>
    <div class="fpt"><span class="box"></span><div class="fpt-img" style="background:linear-gradient(135deg,#777,#222)" role="img" aria-label="Pack of black straps and buckles"></div><div><h4>132 IN Starps &amp; Buckle Packs</h4><small>FREE!</small><strong>$ 26.14</strong></div></div>
  </aside>

  <aside class="side indoor center" style="top:1395px;height:355px">
    <div class="side-head">Looking for an indoor cover?</div>
    <div class="indoor-img" role="img" aria-label="Blue boat cover on a trailer"></div>
    <h4>Mooring 600 Denier Boat Cover<br>Fits V- Hull Runabou</h4>
    <p class="reg">Regular price: <s>$ 300</s></p>
    <p class="deal">$138.81</p>
  </aside>

  <aside class="side ebook" style="top:1774px;height:208px">
    <div class="ebook-top">
      <svg width="58" height="58" viewBox="0 0 58 58"><path d="M6 24L29 6l23 18v26H6z" fill="#fff" stroke="#555" stroke-width="2.5"/><path d="M6 24l23 16 23-16" fill="none" stroke="#555" stroke-width="2.5"/><circle cx="10" cy="46" r="9" fill="#555"/><path d="M5.5 46l3 3.5 6-7" fill="none" stroke="#fff" stroke-width="2.2"/></svg>
      <div><h4>Get a Free E-Book</h4><small>Just enter your email address</small></div>
    </div>
    <div class="field"></div>
    <div class="submit">SUBMIT</div>
  </aside>

  <div class="hills" role="img" aria-label="Soft blue mountain range footer"></div>
</div>
</body>
</html>
```